Shop front signage design for Bubble Tea Shop

Tapioca Grove is Sydney based Green Tea Shop.We are looking for a modern and sleek signage for shop front end. We have Aluminium Composite Panel and Awning sign at the shop front. We will keep Aluminium composite panel simple with logo and text. We are after awning design which is above glass door and under the panel. Old Awning is PVC foam in two pieces 2310mm w x 1000mm h. We need someone to design awing. It should reflect Bubble tea and using bubble tea cups with pearls is essential. Stock images can be used. Avoid using icons or illustrative icons as we are after real images of bubble tea cup. This is to ensure that the brand is not taken as juice shop or cafe.
Panel Dimensions is 5250 mm w x 580 mm h.Awning/ Fascia sign is 4720 mm w x 1000 mm h.
Logo and signage concept is attached.

Target Market(s)

Corporate Male and Female, school, general public.

Colors
f36e22
333333
000000
eaeaea
cbcbcb

Requirements
Must have
• Bubble tea cups with fruit or milk tea.
Should not have
• Icons, illustration

```html
<!DOCTYPE html>
<html lang="en">
<head>
<meta charset="utf-8">
<title>Tapioca Grove – Awning Sign</title>
<link href="https://fonts.googleapis.com/css2?family=Roboto:wght@400;500;700&display=swap" rel="stylesheet">
<style>
  :root {
    --brand-orange: #f36e22;
    --ink: #000000;
    --charcoal: #333333;
    --page-grey: #eaeaea;
    --panel-white: #ffffff;
  }
  html, body {
    margin: 0;
    padding: 0;
    width: 1200px;
    height: 1000px;
    overflow: hidden;
    background: var(--page-grey);
    font-family: "Roboto", Arial, sans-serif;
  }
  .awning {
    position: absolute;
    left: 57px;
    top: 419px;
    width: 1080px;
    height: 228px;
    background: var(--panel-white);
    overflow: hidden;
  }
  .awning__shapes {
    position: absolute;
    inset: 0;
  }
  .awning__cups {
    position: absolute;
    left: 45px;
    top: 14px;
    width: 175px;
    height: 198px;
    border-radius: 10px;
    background: linear-gradient(100deg, #9a7bc0 0%, #b58fcf 30%, #f0a7b8 50%, #e9a0b2 65%, #d9d85a 85%, #c9cf3e 100%);
  }
  .awning__brand {
    position: absolute;
    left: 322px;
    top: 0;
    width: 440px;
    height: 228px;
    display: flex;
    align-items: center;
    gap: 16px;
  }
  .brand__dot {
    width: 84px;
    height: 84px;
    border: 5px solid var(--panel-white);
    border-radius: 50%;
    box-sizing: border-box;
    flex: none;
  }
  .brand__name {
    color: var(--panel-white);
    font-weight: 500;
    font-size: 46px;
    letter-spacing: -0.5px;
    white-space: nowrap;
  }
  .awning__menu {
    position: absolute;
    left: 876px;
    top: 49px;
    margin: 0;
    padding: 0;
    list-style: none;
  }
  .menu__label {
    font-size: 15px;
    font-weight: 400;
    color: var(--ink);
    letter-spacing: 0.5px;
    margin: 0 0 3px 15px;
  }
  .menu__item {
    display: flex;
    align-items: center;
    gap: 6px;
    font-size: 21px;
    font-weight: 700;
    color: var(--ink);
    line-height: 28px;
  }
  .menu__item::before {
    content: "";
    width: 9px;
    height: 9px;
    background: var(--brand-orange);
    flex: none;
  }
</style>
</head>
<body>
  <section class="awning" aria-label="Tapioca Grove awning sign">
    <svg class="awning__shapes" viewBox="0 0 1080 228" width="1080" height="228" aria-hidden="true">
      <polygon points="240,0 840,0 763,228 318,228" fill="var(--brand-orange)"/>
      <g stroke="var(--brand-orange)" stroke-width="2.5">
        <line x1="213" y1="0" x2="291" y2="228"/>
        <line x1="222" y1="0" x2="300" y2="228"/>
        <line x1="231" y1="0" x2="309" y2="228"/>
        <line x1="867" y1="0" x2="789" y2="228"/>
        <line x1="858" y1="0" x2="780" y2="228"/>
        <line x1="849" y1="0" x2="771" y2="228"/>
      </g>
    </svg>

    <div class="awning__cups" role="img" aria-label="Photo of three bubble tea cups with domed lids, blue straws and tapioca pearls: taro, strawberry milk and mango"></div>

    <div class="awning__brand">
      <span class="brand__dot"></span>
      <span class="brand__name">Tapioca Grove</span>
    </div>

    <div class="awning__menu">
      <p class="menu__label">SERVING</p>
      <ul style="margin:0;padding:0;list-style:none">
        <li class="menu__item">PEARL TEA</li>
        <li class="menu__item">FRUIT TEA</li>
        <li class="menu__item">GREEN TEA</li>
        <li class="menu__item">ICE FRAPPE</li>
      </ul>
    </div>
  </section>
</body>
</html>
```